Rack Card Design for an Ayurvedic Beauty Product Project

Hello, I need to have rack cards. The rack cards would be about 3 products we are showcasing at an event. I am a cosmetic company. I have a logo and basic design ideas. I have attached some product images and info. By no means am I a designer so please excuse my messy AI files. Please feel free to design this as feminine as you like. :)

Target Market(s)

Beauty industry, organic, holistic, ayurveda

Industry/Entity Type

Cosmetic

```html
<!DOCTYPE html>
<html lang="en">
<head>
<meta charset="utf-8">
<title>Sarvelle Botanica Rack Cards</title>
<link href="https://fonts.googleapis.com/css2?family=Quicksand:wght@500;600&family=Montserrat:wght@700&family=Open+Sans:wght@400;600&display=swap" rel="stylesheet">
<style>
  :root {
    --plum: #7a1a5c;
    --plum-deep: #4a0f3a;
    --gold: #c9a26b;
    --gold-dark: #8a6238;
    --gold-light: #e6cfa4;
    --ink: #3a2a33;
    --paper: #ffffff;
    --backdrop: #b9b9b9;
    --photo-teal: #2f6a6d;
  }
  * { box-sizing: border-box; margin: 0; padding: 0; }
  html, body { width: 708px; height: 1200px; overflow: hidden; }
  body {
    background: linear-gradient(180deg, #cfcfcf 0%, var(--backdrop) 100%);
    font-family: "Open Sans", sans-serif;
    position: relative;
  }
  .rack-card {
    position: absolute;
    top: 239px;
    width: 322px;
    height: 722px;
    background: var(--paper);
    overflow: hidden;
    box-shadow: 6px 10px 22px rgba(0,0,0,.35);
  }
  .rack-card--front { left: 20px; }
  .rack-card--back { left: 366px; }

  /* front */
  .hero-photo {
    position: absolute; left: 0; top: 0; width: 322px; height: 250px;
    background: radial-gradient(ellipse at 65% 40%, #7d6a5e 0%, #3f7c7e 45%, var(--photo-teal) 100%);
  }
  .hero-wave { position: absolute; left: 0; top: 175px; width: 322px; height: 110px; }
  .brand-mark {
    position: absolute; left: 18px; top: 262px;
    display: flex; flex-direction: column; align-items: center; gap: 6px;
  }
  .brand-mark__dot { width: 52px; height: 52px; border-radius: 50%; background: var(--gold); }
  .brand-mark__name {
    font-family: "Open Sans", sans-serif; font-weight: 600; font-size: 8.5px;
    color: var(--gold-dark); letter-spacing: .4px; white-space: nowrap;
  }
  .product-trio {
    position: absolute; left: 78px; top: 340px; width: 166px; height: 168px;
    border-radius: 6px;
    background: linear-gradient(180deg, #a02a7c 0%, #7a1a5c 70%, #d9c19a 100%);
  }
  .brand-intro {
    position: absolute; left: 20px; top: 520px; width: 282px;
    font-size: 9.4px; line-height: 11.6px; color: var(--ink); text-align: center;
  }
  .brand-intro strong { color: var(--gold-dark); font-weight: 600; }
  .phone-pill {
    position: absolute; left: 16px; top: 636px; width: 290px; height: 46px;
    border-radius: 23px;
    background: linear-gradient(90deg, #9a7040 0%, #d7b57f 55%, #a57a45 100%);
    display: flex; align-items: center; justify-content: center; gap: 10px;
    color: #fff; font-family: "Open Sans", sans-serif; font-size: 30px; letter-spacing: .5px;
  }
  .card-footer { position: absolute; left: 0; bottom: 0; width: 322px; height: 38px; }
  .card-footer__link {
    position: absolute; left: 0; right: 0; bottom: 8px;
    display: flex; align-items: center; justify-content: center; gap: 6px;
    font-size: 12px; color: var(--ink);
  }
  .rack-card--front .card-footer__link { color: #fff; }

  /* back */
  .list-header { position: absolute; left: 0; top: 0; width: 322px; height: 110px; }
  .list-title {
    position: absolute; left: 0; right: 0; top: 20px; text-align: center;
    font-family: "Quicksand", sans-serif; font-weight: 500; font-size: 29px;
    color: var(--plum-deep); line-height: 1; white-space: nowrap;
  }
  .list-subtitle {
    position: absolute; left: 0; right: 0; top: 56px; text-align: center;
    font-family: "Montserrat", sans-serif; font-weight: 700; font-size: 18px; color: var(--plum-deep);
  }
  .product-row { position: absolute; left: 0; top: 0; width: 322px; }
  .product-row__image {
    position: absolute; left: 30px; width: 72px;
    background: linear-gradient(180deg, #a02a7c 0%, #7a1a5c 75%, #d9c19a 100%);
    border-radius: 4px;
  }
  .product-row__name {
    position: absolute; left: 134px; width: 176px;
    font-family: "Quicksand", sans-serif; font-weight: 600; font-size: 13px; line-height: 17px;
    color: var(--plum-deep);
  }
  .product-row__text {
    position: absolute; left: 134px; width: 170px;
    font-size: 9px; line-height: 12.5px; color: var(--ink);
  }
  .divider {
    position: absolute; left: 24px; width: 298px; height: 3px;
    background: linear-gradient(90deg, rgba(122,26,92,0) 0%, var(--plum) 40%, var(--plum) 100%);
  }
  .footer-rule { position: absolute; left: 0; bottom: 0; width: 322px; height: 4px; background: var(--plum); }
</style>
</head>
<body>

  <section class="rack-card rack-card--front">
    <div class="hero-photo" role="img" aria-label="Photo of a woman with long wet dark hair in a teal top against a misty teal backdrop"></div>
    <svg class="hero-wave" viewBox="0 0 322 110" preserveAspectRatio="none" aria-hidden="true">
      <path d="M0 40 C80 60 150 95 230 70 C270 58 300 50 322 52 L322 110 L0 110 Z" fill="#d8be8e"/>
      <path d="M0 52 C80 70 150 100 230 80 C270 70 300 62 322 62 L322 110 L0 110 Z" fill="#8a6238"/>
      <path d="M0 60 C80 78 150 106 230 88 C270 78 300 72 322 72 L322 110 L0 110 Z" fill="#ffffff"/>
    </svg>

    <div class="brand-mark">
      <span class="brand-mark__dot"></span>
      <span class="brand-mark__name">SARVELLE BOTANICA</span>
    </div>

    <div class="product-trio" role="img" aria-label="Product shot: two plum tubes with gold caps and a white cream jar"></div>

    <p class="brand-intro"><strong>Sarvelle Botanica</strong> curates organic infused products where holistic skin care meets a luxurious experience. Each ingredient is carefully selected; providing Ayurvedic herbs, rich minerals &amp; elements. Stimulating hydration and anti-oxidants to lift, firm and illuminate your skin. We believe in connecting with your inner mantra, stimulating higher vibrations, self-esteem, positive mind and soul. As a brand we work with our experts/suppliers of Ayurveda to ensure that our products meet the quality, wholesome healing that you need.</p>

    <div class="phone-pill">
      <svg width="30" height="30" viewBox="0 0 30 30" aria-hidden="true">
        <circle cx="15" cy="15" r="13" fill="none" stroke="#fff" stroke-width="2"/>
        <path d="M10 8 l3 0 l1.5 4 l-2 1.5 c1 2.2 2.5 3.7 4.5 4.5 l1.5 -2 l4 1.5 l0 3 c-7 1 -13 -5 -12.5 -12.5z" fill="#fff"/>
      </svg>
      <span>0100-246-810</span>
    </div>

    <svg class="card-footer" viewBox="0 0 322 38" preserveAspectRatio="none" aria-hidden="true">
      <path d="M0 14 C100 2 222 2 322 14 L322 38 L0 38 Z" fill="#9a7040"/>
      <rect x="0" y="34" width="322" height="4" fill="#4a0f3a"/>
    </svg>
    <div class="card-footer__link">
      <svg width="11" height="11" viewBox="0 0 12 12" aria-hidden="true"><circle cx="6" cy="6" r="5" fill="none" stroke="currentColor"/><ellipse cx="6" cy="6" rx="2.2" ry="5" fill="none" stroke="currentColor"/><line x1="1" y1="6" x2="11" y2="6" stroke="currentColor"/></svg>
      <span>www.sarvellebotanica.com</span>
    </div>
  </section>

  <section class="rack-card rack-card--back">
    <svg class="list-header" viewBox="0 0 322 110" preserveAspectRatio="none" aria-hidden="true">
      <path d="M0 0 L322 0 L322 40 C300 70 220 80 185 90 C172 94 165 100 161 108 C157 100 150 94 137 90 C102 80 22 70 0 40 Z" fill="#c9a26b"/>
      <path d="M6 0 L316 0 L316 36 C294 64 216 74 183 84 C171 88 165 94 161 100 C157 94 151 88 139 84 C106 74 28 64 6 36 Z" fill="#ffffff"/>
    </svg>
    <h1 class="list-title">Sarvelle Botanica</h1>
    <h2 class="list-subtitle">Product List</h2>

    <article class="product-row">
      <div class="product-row__image" style="top:126px;height:146px" role="img" aria-label="Plum tube of firming breast toner with gold cap"></div>
      <h3 class="product-row__name" style="top:140px">Sarvelle Botanica Firming and Lifting Breast Toner</h3>
      <p class="product-row__text" style="top:200px">Using all natural Ayurvedic herbs, our breast toner, prepares the area for maximum absorption, giving you the best results and the most invigorating treatment</p>
    </article>
    <div class="divider" style="top:284px"></div>

    <article class="product-row">
      <div class="product-row__image" style="top:300px;height:158px;border-radius:36px 36px 6px 6px;background:linear-gradient(180deg,#7a1a5c 0%,#a02a7c 35%,#f2f0f0 55%,#d9c19a 100%)" role="img" aria-label="Plum lid and white jar of firming breast cream"></div>
      <h3 class="product-row__name" style="top:320px">Sarvelle Botanica Firming and Lifting Breast Cream</h3>
      <p class="product-row__text" style="top:396px">Using all natural Ayurvedic herbs, our breast cream helps enhance, tighten, and lift your breast</p>
    </article>
    <div class="divider" style="top:476px"></div>

    <article class="product-row">
      <div class="product-row__image" style="top:496px;height:170px;width:56px;left:38px" role="img" aria-label="Slim plum tube of toning breast serum with gold cap"></div>
      <h3 class="product-row__name" style="top:500px">Sarvelle Botanica Firming and Toning Breast Serum</h3>
      <p class="product-row__text" style="top:560px">Using all natural Ayurvedic herbs, and a touch of 24k gold, our serum enhances the experience and quality of results when partnered with the Sarvelle Botanica Firming and Lifting Breast Cream providing an all-day boosting experience</p>
    </article>

    <div class="card-footer__link" style="bottom:10px">
      <svg width="11" height="11" viewBox="0 0 12 12" aria-hidden="true"><circle cx="6" cy="6" r="5" fill="none" stroke="currentColor"/><ellipse cx="6" cy="6" rx="2.2" ry="5" fill="none" stroke="currentColor"/><line x1="1" y1="6" x2="11" y2="6" stroke="currentColor"/></svg>
      <span>www.sarvellebotanica.com</span>
    </div>
    <div class="footer-rule"></div>
  </section>

</body>
</html>
```